Flyer LMTG

Everyone deserves true happiness.
Real Food is the answer to:
A body you love
Reverting illnesses
Healthy digestion
Stable blood sugar
Emotions in control
Blasting energy
Sound sleep
REAL food + water + exercise + Laughter =
“HIGH QUALITY OF LIFE “
EASY, right?
Challenging: certainly
Changing habits: reluctance in sight!
WE’RE OFFER TO:
1. Study YOUR unique body composition, food cravings, blockages, illnesses, and personality!
2. Introduce you to new Food
3. customized wellness plan with follow ups
4. meditation,cooking, and fitness classes as well as wellness workshops
5. New friends with high aspirations
LOGO
Contact info
Please visit our web address to see our design style and colors: www.larkmosstideglow.net
Target Market(s)
people who want to be more healthy
Industry/Entity Type
Fitness
Requirements
Must have
- beautiful pictures of fresh food (main picture) and maybe a few more small pictures reflecting
exercise
healthy living
meditation
Nice to have
- look is crucial. recall some of the color or colors from my logo to have a theme

```html
<!DOCTYPE html>
<html lang="en">
<head>
<meta charset="utf-8">
<title>LMTG Flyer</title>
<link href="https://fonts.googleapis.com/css2?family=PT+Sans:ital,wght@0,400;0,700;1,400;1,700&display=swap" rel="stylesheet">
<style>
  :root {
    --stage: #1c1e1f;
    --leaf: #0b8535;
    --orange: #e68a1c;
    --paper: #ffffff;
    --back-paper: #f7f7f7;
    --ink: #1a1a1a;
    --on-leaf: #ffffff;
    --brand-green: #2f8a2a;
  }
  * { margin: 0; padding: 0; box-sizing: border-box; }
  html, body { width: 900px; height: 1200px; overflow: hidden; background: var(--stage); }
  .canvas { position: relative; width: 900px; height: 1200px; font-family: "PT Sans", sans-serif; }

  .panel { position: absolute; top: 186px; width: 162px; height: 289px; overflow: hidden; }
  .panel--front { left: 55px; background: var(--paper); border: 3px solid var(--orange); }
  .panel--inner-left { left: 278px; background: var(--leaf); border: 3px solid var(--orange); }
  .panel--inner-right { left: 484px; background: var(--leaf); border: 3px solid var(--orange); }
  .panel--back { left: 675px; background: var(--back-paper); }

  .photo-fruit { position: absolute; left: 14px; top: 6px; width: 134px; height: 110px; }
  .photo-active { position: absolute; left: 2px; top: 104px; width: 152px; height: 92px; }

  .brand { position: absolute; display: flex; align-items: center; gap: 5px; }
  .brand__dot { width: 26px; height: 26px; border-radius: 50%; background: var(--orange); flex: none; }
  .brand__name { font-size: 21px; font-weight: 400; color: var(--brand-green); letter-spacing: 0.5px; }
  .panel--front .brand { left: 8px; top: 232px; }
  .panel--inner-left .brand, .panel--inner-right .brand { left: 8px; top: 240px; }
  .panel--inner-left .brand__name, .panel--inner-right .brand__name { color: var(--on-leaf); }
  .panel--back .brand { left: 14px; top: 100px; }

  .web { position: absolute; font-size: 5.5px; font-weight: 700; color: var(--ink); }
  .panel--inner-left .web, .panel--inner-right .web { right: 6px; bottom: 3px; color: var(--on-leaf); }
  .panel--back .web { left: 0; right: 0; top: 145px; text-align: center; font-size: 6px; }

  .copy { position: absolute; left: 5px; right: 5px; text-align: center; font-style: italic; color: var(--on-leaf); }
  .copy--benefits { top: 44px; font-size: 7.4px; line-height: 10px; font-weight: 700; }
  .copy--benefits .gap { height: 9px; }
  .copy--challenge { top: 36px; font-size: 8px; line-height: 11px; font-weight: 700; }
  .copy--challenge .gap { height: 10px; }
  .copy--offer { top: 122px; font-size: 5.4px; line-height: 7.2px; font-style: normal; font-weight: 700; }
  .copy--offer ol { list-style: none; margin-top: 2px; }

  .label { position: absolute; top: 514px; height: 23px; background: var(--paper); color: var(--ink);
           font-size: 11px; font-weight: 700; font-style: italic; display: flex; align-items: center; justify-content: center; }
  .label--front { left: 87px; width: 56px; }
  .label--inner-left { left: 321px; width: 81px; }
  .label--inner-right { left: 522px; width: 84px; }
  .label--back { left: 723px; width: 44px; }
</style>
</head>
<body>
<main class="canvas">

  <section class="panel panel--front">
    <svg class="photo-fruit" viewBox="0 0 134 110" role="img" aria-label="Photo of assorted fresh fruit: melon, papaya, grapes, pineapple and oranges">
      <defs>
        <radialGradient id="fruitTones" cx="50%" cy="50%" r="65%">
          <stop offset="0%" stop-color="#e9a43a"/>
          <stop offset="55%" stop-color="#c8642a"/>
          <stop offset="100%" stop-color="#f4efe4"/>
        </radialGradient>
      </defs>
      <rect width="134" height="110" rx="6" fill="url(#fruitTones)"/>
    </svg>
    <svg class="photo-active" viewBox="0 0 152 92" role="img" aria-label="Photos of a forest landscape and people exercising outdoors">
      <defs>
        <linearGradient id="activeTones" x1="0" y1="0" x2="1" y2="1">
          <stop offset="0%" stop-color="#5f8f4a"/>
          <stop offset="60%" stop-color="#8fb46a"/>
          <stop offset="100%" stop-color="#c9d9b0"/>
        </linearGradient>
      </defs>
      <polygon points="4,26 52,6 74,66 40,82" fill="url(#activeTones)"/>
      <polygon points="50,40 112,2 148,60 94,90" fill="url(#activeTones)"/>
    </svg>
    <div class="brand"><span class="brand__dot"></span><span class="brand__name">LMTG</span></div>
  </section>

  <section class="panel panel--inner-left">
    <div class="copy copy--benefits">
      <p>Everyone deserves true happiness.</p>
      <p>Real Food is the answer to:</p>
      <p>A body you love</p>
      <p>Reverting illnesses</p>
      <p>Healthy digestion</p>
      <p>Stable blood sugar</p>
      <p>Emotions in control</p>
      <p>Blasting energy</p>
      <p>Sound sleep</p>
      <div class="gap"></div>
      <p>REAL food + water + exercise + L.O.L. =</p>
      <p>“HIGH QUALITY OF LIFE ”</p>
    </div>
    <div class="brand"><span class="brand__dot"></span><span class="brand__name">LMTG</span></div>
    <p class="web">www.larkmosstideglow.net</p>
  </section>

  <section class="panel panel--inner-right">
    <div class="copy copy--challenge">
      <p>EASY, right?</p>
      <p>Challenging: certainly</p>
      <div class="gap"></div>
      <p>Changing habits: reluctance in sight!</p>
    </div>
    <div class="copy copy--offer">
      <p>WE’RE HERE TO:</p>
      <ol>
        <li>1. Study YOUR unique body composition, food cravings, blockages, illnesses, and personality!</li>
        <li>2. Educate - guide - develop plan - and follow you up 24/7</li>
        <li>3. You will: taste new food, plan meals, groceries shopping.</li>
        <li>4. You’ll attend: meditation, cooking, and fitness classes</li>
        <li>5. You’ll make new friends.</li>
      </ol>
    </div>
    <div class="brand"><span class="brand__dot"></span><span class="brand__name">LMTG</span></div>
    <p class="web">www.larkmosstideglow.net</p>
  </section>

  <section class="panel panel--back">
    <div class="brand"><span class="brand__dot"></span><span class="brand__name">LMTG</span></div>
    <p class="web">www.larkmosstideglow.net</p>
  </section>

  <span class="label label--front">Front side</span>
  <span class="label label--inner-left">Inner left side</span>
  <span class="label label--inner-right">Inner right side</span>
  <span class="label label--back">Backside</span>

</main>
</body>
</html>
```